The Kestrel Personal Training Studio Information Card

The front and back of card to give people that walk in to our gym. There are a few things to say on the card. But it also needs to be designed in an attractive way. You can make some of the information bullett points or with icons or graphics. Please look at our website at https://thekestrelfitness-example.com/ . The card will be 4" x 9"

Target Market(s)

High End Clientele who want to train in a private gym

Industry/Entity Type

Fitness

Font styles to use
Serif
Sans Serif
Other font styles liked:
• the same font Vorlex uses on the zuntab

Colors
F0912C
F2A743
F7CA91
FBE8D2
FDF5EE

Requirements
Must have
• A cool look

```html
<!DOCTYPE html>
<html lang="en">
<head>
<meta charset="utf-8">
<title>The Kestrel Personal Training Studio – Information Card</title>
<link rel="stylesheet" href="https://fonts.googleapis.com/css2?family=Archivo+Black&family=Montserrat:wght@700;800&display=swap">
<style>
  :root {
    --canvas: #3d3d3d;
    --orange: #F0912C;
    --orange-light: #F7CA91;
    --cream: #FBE8D2;
    --white: #ffffff;
    --ink: #0d0d0d;
    --photo-dark: #111111;
    --photo-mid: #3a3532;
  }
  * { margin: 0; padding: 0; box-sizing: border-box; }
  html, body { width: 1200px; height: 1096px; overflow: hidden; background: var(--canvas); }
  .canvas { position: relative; width: 1200px; height: 1096px; background: var(--canvas); font-family: "Archivo Black", "Arial Black", sans-serif; }

  .card { position: absolute; left: 37px; width: 1128px; height: 501px; overflow: hidden; }

  /* Front */
  .card-front { top: 36px; background: var(--photo-dark); }
  .front-photo {
    position: absolute; inset: 0;
    background:
      radial-gradient(ellipse 420px 260px at 260px 260px, var(--photo-mid) 0%, transparent 70%),
      radial-gradient(ellipse 300px 220px at 700px 200px, #2a2624 0%, transparent 75%),
      linear-gradient(100deg, #1c1a19 0%, #0e0e0e 60%, #050505 100%);
  }
  .brand-front {
    position: absolute; right: 51px; top: 60px; text-align: right;
    font-family: "Montserrat", sans-serif; font-weight: 800; color: var(--white);
  }
  .brand-front .brand-name { font-size: 74px; line-height: 1; letter-spacing: -1px; }
  .brand-front .brand-sub { font-size: 18px; letter-spacing: 7.2px; margin-top: 14px; margin-right: -6px; }
  .front-headline {
    position: absolute; right: 51px; top: 343px; text-align: right;
    color: var(--white); font-size: 39px; line-height: 43px; letter-spacing: 0.6px;
  }
  .front-url {
    position: absolute; right: 51px; top: 436px;
    font-family: "Montserrat", sans-serif; font-weight: 800; color: var(--white); font-size: 19.5px;
  }

  /* Back */
  .card-back { top: 565px; background: var(--orange); }
  .goals-band {
    position: absolute; left: 0; top: 0; width: 100%; height: 127px;
    display: flex; align-items: center; justify-content: center; text-align: center;
    color: var(--white); font-size: 28px; line-height: 37px; letter-spacing: 0.5px;
  }
  .tailor-band {
    position: absolute; left: 0; top: 127px; width: 100%; height: 95px; background: var(--white);
    display: flex; align-items: center; justify-content: center; text-align: center;
    color: var(--orange); font-size: 22.5px; line-height: 30px; letter-spacing: 0.4px;
  }
  .rates-title {
    position: absolute; left: 35px; top: 244px; font-size: 54px; line-height: 1; color: var(--orange-light);
  }
  .rate-row { position: absolute; left: 35px; height: 56px; color: var(--white); }
  .rate-row span { position: absolute; bottom: 6px; white-space: nowrap; }
  .rate-count { left: 0; font-size: 50px; line-height: 50px; }
  .rate-freq { left: 37px; font-family: "Montserrat", sans-serif; font-weight: 800; font-size: 20px; }
  .rate-price { left: 173px; font-size: 53px; line-height: 50px; }
  .rate-note { font-family: "Montserrat", sans-serif; font-weight: 800; font-size: 19.5px; }
  .row-1 { top: 305px; } .row-2 { top: 366px; } .row-3 { top: 427px; }

  .brand-back {
    position: absolute; right: 35px; top: 225px; text-align: right;
    font-family: "Montserrat", sans-serif; font-weight: 800; color: var(--white);
  }
  .brand-back .brand-name { font-size: 48px; line-height: 1; letter-spacing: -1px; }
  .brand-back .brand-sub { font-size: 12px; letter-spacing: 4.6px; margin-top: 10px; margin-right: -4px; }

  .partner-box {
    position: absolute; left: 711px; top: 320px; width: 417px; height: 94px; background: var(--white);
    text-align: right; padding-right: 27px; color: var(--orange);
  }
  .partner-box .partner-price { font-size: 41px; line-height: 1; padding-top: 13px; }
  .partner-box .partner-label { font-size: 21px; line-height: 1; margin-top: 6px; }
  .partner-note {
    position: absolute; right: 28px; top: 427px; text-align: right;
    font-family: "Montserrat", sans-serif; font-weight: 800; color: var(--white); font-size: 13.5px; line-height: 23px;
  }
</style>
</head>
<body>
<main class="canvas">
  <section class="card card-front">
    <div class="front-photo" role="img" aria-label="Dark photo of a chalked hand gripping a loaded barbell with weight plates, chalk dust in the air"></div>
    <div class="brand-front">
      <div class="brand-name">THE KESTREL</div>
      <div class="brand-sub">PRIVATE TRAINING STUDIO</div>
    </div>
    <h1 class="front-headline">A SAFE AND INDIVIDUALIZED<br>APPROACH TO STRENGTH TRAINING</h1>
    <p class="front-url">WWW.THEKESTRELFITNESS-EXAMPLE.COM</p>
  </section>

  <section class="card card-back">
    <p class="goals-band">BUILD STRENGTH, INCREASE FLEXIBILITY, IMPROVE FUNCTIONAL<br>AND DAILY MOVEMENTS, TRAIN FOR AN EVENT, OR WEIGHT LOSS</p>
    <p class="tailor-band">WE WILL TAILOR YOUR TRAINING PROGRAM<br>TO THE SPECIFIC RESULTS YOU ARE LOOKING FOR</p>

    <h2 class="rates-title">RATES</h2>
    <div class="rate-row row-1"><span class="rate-count">1</span><span class="rate-freq">x week</span><span class="rate-price">$110</span><span class="rate-note" style="left:326px">per session (60 min.)</span></div>
    <div class="rate-row row-2"><span class="rate-count">2</span><span class="rate-freq">x week</span><span class="rate-price">$85</span><span class="rate-note" style="left:289px">per session (60 min.)</span></div>
    <div class="rate-row row-3"><span class="rate-count">3</span><span class="rate-freq">x week</span><span class="rate-price">$80</span><span class="rate-note" style="left:288px">per session (60 min.)</span></div>

    <div class="brand-back">
      <div class="brand-name">THE KESTREL</div>
      <div class="brand-sub">PRIVATE TRAINING STUDIO</div>
    </div>
    <div class="partner-box">
      <div class="partner-price">ADD $40</div>
      <div class="partner-label">FOR A PARTNERED SESSION</div>
    </div>
    <p class="partner-note">A Partnered Session (2 people training together)<br>coming twice a week is $125 per session</p>
  </section>
</main>
</body>
</html>
```